Door Hanger for 20% off on dry cleaning

I need a door hanger (3.5" x 8.5" with a hole for the door handle) for a 20% off sale on dry cleaning. The business is called "Suds by Maplecrest" and is a full-service laundry. The store is a laundromat that is used by self-serve customers. We also do wash-and-fold laundry and dry cleaning.

Some requirements:
* Include the logo
* Includes the address of the business:
615 South 300 West
Provo, Utah
(behind Harbor Crust Pies)
* Include some indication of our other services (wash-and-fold laundry, coin laundry, comforters cleaned)
* Offer needs to include an expiration date (say, September 30, 2014).

The door hanger should be full-color with designs for both sides.
Updates

The sale is for 20% off of Dry Cleaning - not the other services. And I'd like both sides of the hanger to mention the sale - in case it gets hung backwards on the door.

Industry/Entity Type

Dry Cleaning

```html
<!DOCTYPE html>
<html lang="en">
<head>
<meta charset="utf-8">
<title>Suds by Maplecrest – Door Hanger</title>
<link href="https://fonts.googleapis.com/css2?family=Roboto+Condensed:wght@400;700;800;900&display=swap" rel="stylesheet">
<style>
  :root{
    --bg:#e4e5e7;
    --paper:#f7f7f8;
    --paper-edge:#e9eaec;
    --navy:#1f3c8c;
    --blue:#2160b8;
    --blue-light:#2aa4e2;
    --sky:#9fd3ea;
    --lime:#a9cf3a;
    --orange:#f26522;
    --white:#ffffff;
  }
  *{box-sizing:border-box;margin:0;padding:0}
  html,body{width:933px;height:1200px;overflow:hidden}
  body{background:var(--bg);font-family:"Roboto Condensed",Arial,sans-serif;position:relative}

  .hanger{
    position:absolute;top:140px;width:380px;height:920px;overflow:hidden;
    background:linear-gradient(180deg,var(--paper) 0%,var(--paper-edge) 60%);
    box-shadow:0 6px 18px rgba(0,0,0,.18);
  }
  .hanger--front{left:58px}
  .hanger--back{left:495px}

  .handle-hole{position:absolute;left:112px;top:32px;width:156px;height:156px;border-radius:50%;
    border:2px dashed var(--blue);padding:6px}
  .handle-hole span{display:block;width:100%;height:100%;border-radius:50%;
    background:linear-gradient(135deg,var(--blue) 0%,var(--blue-light) 100%)}

  .brand{position:absolute;top:232px;left:0;right:0;display:flex;justify-content:center;align-items:center;gap:10px}
  .brand__dot{width:22px;height:22px;border-radius:50%;background:var(--blue)}
  .brand__name{font-size:36px;font-weight:700;color:var(--navy);letter-spacing:.2px}

  .address{position:absolute;top:300px;left:0;right:0;text-align:center;color:var(--navy);
    font-weight:800;font-size:18px;line-height:1.3;text-transform:uppercase;letter-spacing:.6px}
  .address svg{width:13px;height:17px;vertical-align:-2px;margin-right:4px}

  .divider{position:absolute;top:388px;left:125px;width:130px;height:6px}

  .services{position:absolute;top:402px;left:0;right:0;text-align:center;color:var(--orange);
    font-weight:800;font-size:28px;line-height:1.15;text-transform:uppercase}

  .waves{position:absolute;left:0;top:520px;width:380px;height:400px}

  .tag{position:absolute;left:8px;top:612px;width:310px;height:168px;transform:rotate(-25deg);transform-origin:50% 50%}
  .tag__shape{position:absolute;left:0;top:0;width:310px;height:168px;overflow:visible}
  .tag span{position:absolute;color:var(--white);font-weight:900;text-transform:uppercase;line-height:.9;white-space:nowrap}
  .tag .tag__the{left:40px;top:10px;font-size:36px}
  .tag .tag__sale{left:16px;top:42px;font-size:70px;letter-spacing:-1px}
  .tag .tag__isfor{left:28px;top:112px;font-size:24px;line-height:.95}
  .tag .tag__pct{left:82px;top:100px;font-size:66px;letter-spacing:-2px}
  .tag .tag__pctsign{left:166px;top:96px;font-size:34px}
  .tag .tag__off{left:164px;top:132px;font-size:22px}

  .tag .fine{left:40px;top:178px;width:270px;font-weight:800;font-size:23px;line-height:1.05;text-align:center}

  .expiry{position:absolute;left:150px;top:855px;width:250px;height:34px;transform:rotate(-13deg);
    background:var(--orange);clip-path:polygon(8% 0,100% 0,100% 100%,0 100%);
    color:var(--white);font-weight:800;font-size:16px;letter-spacing:.5px;text-transform:uppercase;
    display:flex;align-items:center;justify-content:center;padding-left:10px}
</style>
</head>
<body>

<section class="hanger hanger--front">
  <div class="handle-hole"><span></span></div>
  <div class="brand"><span class="brand__dot"></span><span class="brand__name">Suds by Maplecrest</span></div>
  <p class="address">
    <svg viewBox="0 0 12 16"><path d="M6 0C2.7 0 0 2.6 0 5.8 0 10 6 16 6 16s6-6 6-10.2C12 2.6 9.3 0 6 0zm0 8.2A2.4 2.4 0 1 1 6 3.4a2.4 2.4 0 0 1 0 4.8z" fill="#1f3c8c"/></svg>615 South 300 West<br>Provo, Utah<br>(Behind Harbor Crust Pies)
  </p>
  <svg class="divider" viewBox="0 0 130 6"><line x1="3" y1="3" x2="127" y2="3" stroke="#1f3c8c" stroke-width="1.5"/><circle cx="3" cy="3" r="2.5" fill="#1f3c8c"/><circle cx="127" cy="3" r="2.5" fill="#1f3c8c"/></svg>
  <p class="services">Wash-and-Fold Laundry<br>Coin Laundry<br>Comforters Cleaned</p>

  <svg class="waves" viewBox="0 0 380 400" preserveAspectRatio="none">
    <defs><linearGradient id="seaA" x1="0" y1="0" x2="1" y2="1"><stop offset="0" stop-color="#3a8fd6"/><stop offset="1" stop-color="#1d4fa6"/></linearGradient></defs>
    <path d="M0 40 C80 5 180 10 260 45 S360 60 380 40 V400 H0Z" fill="#a9cf3a"/>
    <path d="M0 50 C80 18 180 22 260 56 S360 72 380 52 V400 H0Z" fill="#9fd3ea"/>
    <path d="M0 62 C80 32 180 36 260 68 S360 84 380 64 V400 H0Z" fill="#1f3c8c"/>
    <path d="M0 74 C80 46 180 50 260 80 S360 96 380 76 V400 H0Z" fill="url(#seaA)"/>
  </svg>

  <div class="tag">
    <svg class="tag__shape" viewBox="0 0 310 168"><path d="M0 0 H250 L310 84 L250 168 H0Z" fill="#f26522"/><circle cx="262" cy="84" r="11" fill="#fff"/><path d="M262 84 C285 70 300 60 330 40" stroke="#222" stroke-width="2" fill="none"/></svg>
    <span class="tag__the">The</span>
    <span class="tag__sale">Sale</span>
    <span class="tag__isfor">Is<br>For</span>
    <span class="tag__pct">20</span>
    <span class="tag__pctsign">%</span>
    <span class="tag__off">Off</span>
    <span class="fine">Of Dry Cleaning<br>Not the Other Services</span>
  </div>
  <div class="expiry">September 30, 2014</div>
</section>

<section class="hanger hanger--back">
  <div class="handle-hole"><span></span></div>
  <div class="brand"><span class="brand__dot"></span><span class="brand__name">Suds by Maplecrest</span></div>
  <p class="address">
    <svg viewBox="0 0 12 16"><path d="M6 0C2.7 0 0 2.6 0 5.8 0 10 6 16 6 16s6-6 6-10.2C12 2.6 9.3 0 6 0zm0 8.2A2.4 2.4 0 1 1 6 3.4a2.4 2.4 0 0 1 0 4.8z" fill="#1f3c8c"/></svg>615 South 300 West<br>Provo, Utah<br>(Behind Harbor Crust Pies)
  </p>
  <svg class="divider" viewBox="0 0 130 6"><line x1="3" y1="3" x2="127" y2="3" stroke="#1f3c8c" stroke-width="1.5"/><circle cx="3" cy="3" r="2.5" fill="#1f3c8c"/><circle cx="127" cy="3" r="2.5" fill="#1f3c8c"/></svg>
  <p class="services">Wash-and-Fold Laundry<br>Coin Laundry<br>Comforters Cleaned</p>

  <svg class="waves" viewBox="0 0 380 400" preserveAspectRatio="none">
    <defs><linearGradient id="seaB" x1="0" y1="0" x2="1" y2="1"><stop offset="0" stop-color="#3a8fd6"/><stop offset="1" stop-color="#1d4fa6"/></linearGradient></defs>
    <path d="M0 40 C80 5 180 10 260 45 S360 60 380 40 V400 H0Z" fill="#a9cf3a"/>
    <path d="M0 50 C80 18 180 22 260 56 S360 72 380 52 V400 H0Z" fill="#9fd3ea"/>
    <path d="M0 62 C80 32 180 36 260 68 S360 84 380 64 V400 H0Z" fill="#1f3c8c"/>
    <path d="M0 74 C80 46 180 50 260 80 S360 96 380 76 V400 H0Z" fill="url(#seaB)"/>
  </svg>

  <div class="tag">
    <svg class="tag__shape" viewBox="0 0 310 168"><path d="M0 0 H250 L310 84 L250 168 H0Z" fill="#f26522"/><circle cx="262" cy="84" r="11" fill="#fff"/><path d="M262 84 C285 70 300 60 330 40" stroke="#222" stroke-width="2" fill="none"/></svg>
    <span class="tag__the">The</span>
    <span class="tag__sale">Sale</span>
    <span class="tag__isfor">Is<br>For</span>
    <span class="tag__pct">20</span>
    <span class="tag__pctsign">%</span>
    <span class="tag__off">Off</span>
    <span class="fine">Of Dry Cleaning<br>Not the Other Services</span>
  </div>
  <div class="expiry">September 30, 2014</div>
</section>

</body>
</html>
```